I need email signatures for my admin staff members
info:
Darina Qubrosi
Support Coordinator
Unit 4, 517 Wattlebrook Lane, Kemberly NSW 2893
Tel: 02 84427193 Mob: 0427596314
email: darina.qu@mivrotelhaven.com
www.mivrotelhaven.com

Target Market(s)

community services industry

Industry/Entity Type

Community Service

Requirements
Must have
• Specialist Provider of Multicultural Support Services
Nice to have
• "I acknowledge the traditional owners of the land on which we live, work and dream"
plus their flags as attached

```html
<!DOCTYPE html>
<html lang="en">
<head>
<meta charset="utf-8">
<title>Email Signature – Darina Qubrosi</title>
<link rel="stylesheet" href="https://fonts.googleapis.com/css2?family=Montserrat:ital,wght@0,500;0,700;0,800;1,500&display=swap">
<style>
  :root {
    --page-bg: #c2c2c2;
    --brand-orange: #f7901e;
    --panel-grey: #eceeed;
    --pattern-light: #e2e3e3;
    --pattern-dark: #d3d4d4;
    --footer-grey: #8e8e8e;
    --ink: #333333;
    --ink-soft: #444444;
    --white: #ffffff;
  }
  * { margin: 0; padding: 0; box-sizing: border-box; }
  html, body {
    width: 725px; height: 1200px; overflow: hidden;
    background: var(--page-bg);
    font-family: "Montserrat", Arial, sans-serif;
  }
  .signature {
    position: absolute; left: 32px; top: 455px;
    width: 660px; height: 290px;
    background: var(--white);
    box-shadow: 2px 3px 4px rgba(0,0,0,0.18);
    overflow: hidden;
  }
  .top-band {
    position: absolute; left: 0; top: 0; width: 100%; height: 34px;
    background: var(--brand-orange);
  }
  .header-panel {
    position: absolute; left: 0; top: 34px; width: 100%; height: 113px;
    background: var(--panel-grey);
  }
  .header-pattern {
    position: absolute; left: 0; top: 0; width: 361px; height: 113px;
    background: linear-gradient(90deg, var(--pattern-dark) 0%, var(--pattern-light) 75%, var(--panel-grey) 100%);
    clip-path: polygon(0 0, 100% 0, 68% 100%, 0 100%);
  }
  .footer-band {
    position: absolute; left: 0; bottom: 0; width: 100%; height: 17px;
    background: var(--footer-grey);
  }
  .photo-ring {
    position: absolute; left: 27px; top: 42px;
    width: 210px; height: 210px; border-radius: 50%;
    background: var(--white);
  }
  .photo {
    position: absolute; left: 9px; top: 9px;
    width: 192px; height: 192px; border-radius: 50%;
    background: radial-gradient(circle at 45% 55%, #c98a5c 0%, #7a6a7a 45%, #3c4566 80%, #2b2f45 100%);
  }
  .tagline {
    position: absolute; left: 245px; top: 171px;
    width: 217px; height: 74px; border-radius: 10px;
    background: var(--brand-orange);
    color: var(--white);
    font-weight: 800; font-size: 14.5px; line-height: 17px;
    text-align: center; text-transform: uppercase;
    display: flex; align-items: center; justify-content: center;
  }
  .brand {
    position: absolute; left: 483px; top: 48px; width: 160px;
  }
  .brand-mark {
    display: block; width: 54px; height: 54px; border-radius: 50%;
    background: var(--brand-orange);
    margin-left: 45px;
  }
  .brand-name {
    margin-top: 5px;
    color: var(--brand-orange);
    font-weight: 500; font-size: 14.5px; letter-spacing: 0.5px;
    text-transform: uppercase; white-space: nowrap;
  }
  .person {
    position: absolute; left: 483px; top: 154px; width: 170px;
  }
  .person-name {
    color: var(--ink); font-weight: 700; font-size: 12.5px;
    text-transform: uppercase; letter-spacing: 0.2px;
  }
  .person-role {
    color: var(--ink-soft); font-style: italic; font-weight: 500; font-size: 8.3px;
    margin-top: 1px;
  }
  .contact-list { list-style: none; margin-top: 8px; }
  .contact-item {
    display: flex; align-items: flex-start;
    color: var(--ink); font-size: 6.6px; line-height: 8.3px; font-weight: 500;
    margin-bottom: 6.4px;
  }
  .contact-icon { flex: none; width: 9px; height: 9px; margin-right: 6px; }
</style>
</head>
<body>
  <div class="signature">
    <div class="top-band"></div>
    <div class="header-panel">
      <div class="header-pattern" role="img" aria-label="Light grey geometric triangle pattern"></div>
    </div>
    <div class="photo-ring">
      <div class="photo" role="img" aria-label="Photo of two business people shaking hands"></div>
    </div>
    <div class="tagline">Specialist provider of<br>multicultural<br>support services</div>

    <div class="brand">
      <span class="brand-mark"></span>
      <div class="brand-name">Mivrotel Haven</div>
    </div>

    <div class="person">
      <div class="person-name">Darina Qubrosi</div>
      <div class="person-role">Support Coordinator</div>
      <ul class="contact-list">
        <li class="contact-item">
          <svg class="contact-icon" viewBox="0 0 10 10"><circle cx="5" cy="5" r="5" fill="#f7901e"/><path d="M5 2.2a1.8 1.8 0 0 0-1.8 1.8C3.2 5.4 5 7.8 5 7.8S6.8 5.4 6.8 4A1.8 1.8 0 0 0 5 2.2z" fill="#fff"/><circle cx="5" cy="4" r="0.7" fill="#f7901e"/></svg>
          <span>Unit 4, 517 Wattlebrook Lane,<br>Kemberly NSW 2893</span>
        </li>
        <li class="contact-item">
          <svg class="contact-icon" viewBox="0 0 10 10"><circle cx="5" cy="5" r="5" fill="#f7901e"/><path d="M2.6 4.2c0-1 1.1-1.5 2.4-1.5s2.4.5 2.4 1.5l-1 .3-.3-.8H3.9l-.3.8zM3.4 5h3.2l.6 2.3H2.8z" fill="#fff"/></svg>
          <span>02 84427193</span>
        </li>
        <li class="contact-item">
          <svg class="contact-icon" viewBox="0 0 10 10"><circle cx="5" cy="5" r="5" fill="#f7901e"/><rect x="3.5" y="2.2" width="3" height="5.6" rx="0.5" fill="none" stroke="#fff" stroke-width="0.7"/><circle cx="5" cy="6.8" r="0.35" fill="#fff"/></svg>
          <span>0427596314</span>
        </li>
        <li class="contact-item">
          <svg class="contact-icon" viewBox="0 0 10 10"><circle cx="5" cy="5" r="5" fill="#f7901e"/><rect x="2.5" y="3.2" width="5" height="3.6" fill="#fff"/><path d="M2.5 3.2 5 5.2 7.5 3.2" fill="none" stroke="#f7901e" stroke-width="0.5"/></svg>
          <span>darina.qu@mivrotelhaven.com</span>
        </li>
        <li class="contact-item">
          <svg class="contact-icon" viewBox="0 0 10 10"><circle cx="5" cy="5" r="5" fill="#f7901e"/><circle cx="5" cy="5" r="2.6" fill="none" stroke="#fff" stroke-width="0.6"/><ellipse cx="5" cy="5" rx="1.1" ry="2.6" fill="none" stroke="#fff" stroke-width="0.5"/><path d="M2.4 5h5.2" stroke="#fff" stroke-width="0.5"/></svg>
          <span>www.mivrotelhaven.com</span>
        </li>
      </ul>
    </div>

    <div class="footer-band"></div>
  </div>
</body>
</html>
```